Private Maths Tuition Flyer based in London

I am opening up a new Maths tuition centre in North West London. The flyer will be delivered to over 8,000 homes within the immediate vicinity. The design should be suitable to be printed on an A5 sheet and read in a portrait orientation.

The flyer should include the following:

The headline statement should be "Private Maths Tuition"

Secondary headline statement is the following "GCSE, A-Levels, 11 Plus exams"

Some of service offerings/selling points are:

- Free first session
- Monthly Feedback reports
- Free support outside of sessions
- Clear Target grades
- Personalised Lesson plans
- Tangible Results

Another statement that should be featured is "Book your free session by visiting www.lernova.co.uk" or something similar to that.

"Contact Details:
020 4719 8263
enquiries@lernova.co.uk"

"Address:
Kelbridge Business and Innovation Centre
Ashvale Court
Wrenfield Road
HA4 9QD"

Attached you'll see a logo which should be included and also a map of where we are. I am open to new images for the map if you guys have any, rather than a screen shot from google maps but it should be clear to see.

I would like the content above to be displayed in a clear and concise manner that is easy to read. You have creative license on where this information should be displayed and where the images should be but on the whole it should look aesthetically pleasing on the eye.

Target Market(s)

Students, Parents. Parents who want maths tutors.

Industry/Entity Type

Tutoring

Font styles to use
Sans Serif

Requirements
Must have
• *logo*
• Private Maths Tuition
• GCSE, A-Levels, 11 Plus exams
• - Free first session
• - Monthly Feedback reports
• - Free support outside of sessions
• - Clear Target grades
• - Personalised Lesson plans
• - Tangible Results
• Book your free session by visiting www.lernova.co.uk" or something similar to that.
• Contact Details:
• 020 4719 8263
• enquiries@lernova.co.uk
• Address (*with map*):
• Kelbridge Business and Innovation Centre
• Ashvale Court
• Wrenfield Road
• HA4 9QD
Nice to have
• similar colour scheme as the logo. creative background design.

```html
<!DOCTYPE html>
<html lang="en">
<head>
<meta charset="utf-8">
<title>Lernova – Maths Tuition Flyer</title>
<link href="https://fonts.googleapis.com/css2?family=Arimo:wght@400;700&family=Marcellus&family=PT+Sans+Narrow&display=swap" rel="stylesheet">
<style>
  :root {
    --page-bg: #1a1a1a;
    --paper: #ffffff;
    --rule: #c8c8c8;
    --navy: #1d3f8f;
    --royal: #1c4f9c;
    --deep-blue: #2b3494;
    --cyan: #00aeef;
    --orange: #f07228;
    --ink-blue: #1a4aa8;
    --book-light: #f3e3c8;
    --book-mid: #dcb47c;
    --book-deep: #b98246;
    --map-base: #e8e5de;
    --map-park: #d3e4bd;
  }
  * { margin: 0; padding: 0; box-sizing: border-box; }
  html, body { width: 1200px; height: 1200px; overflow: hidden; }
  body { background: var(--page-bg); position: relative; }

  .flyer {
    position: absolute; left: 198px; top: 31px;
    width: 804px; height: 1137px;
    background: var(--paper);
    font-family: "Arimo", Arial, sans-serif;
  }

  .header {
    position: absolute; left: 0; top: 0; width: 100%; height: 154px;
    border-bottom: 1px solid var(--rule);
  }
  .brand {
    position: absolute; left: 64px; top: 76px;
    font-size: 38px; font-weight: 400; line-height: 44px; color: var(--orange);
    display: flex; align-items: center; gap: 10px;
  }
  .brand-dot { width: 14px; height: 14px; border-radius: 50%; background: var(--orange); }
  .header-block {
    position: absolute; top: 62px;
    font-family: "PT Sans Narrow", "Arial Narrow", sans-serif;
    font-size: 13.5px; line-height: 20px; color: var(--navy);
  }
  .contact { left: 320px; }
  .address { left: 522px; }

  .illustration {
    position: absolute; left: 82px; top: 207px; width: 594px; height: 343px;
    background:
      linear-gradient(180deg, rgba(255,255,255,0) 62%, rgba(255,255,255,0) 100%),
      linear-gradient(180deg, #ffffff 0%, #fdfaf5 40%, var(--book-light) 70%, var(--book-mid) 88%, var(--book-deep) 100%);
    border-radius: 4px;
  }

  .headline-band {
    position: absolute; left: 0; top: 588px; width: 522px; height: 148px;
    background: linear-gradient(90deg, var(--deep-blue) 0%, #1e6cc8 55%, var(--cyan) 100%);
  }
  .headline {
    position: absolute; left: 88px; top: 16px;
    font-family: "Marcellus", Georgia, serif; font-weight: 400;
    font-size: 54px; line-height: 57px; color: #fff; white-space: nowrap;
  }
  .subhead {
    position: absolute; left: 542px; top: 682px;
    font-size: 27px; line-height: 28px; color: var(--ink-blue);
  }

  .features {
    position: absolute; left: 52px; top: 751px; width: 700px; height: 82px;
    background: var(--orange); color: #fff;
  }
  .offer {
    position: absolute; left: 0; top: 0; width: 185px; height: 100%;
    background: var(--royal);
    font-weight: 700; font-size: 22px; line-height: 26px;
    padding: 16px 0 0 25px;
  }
  .benefits {
    position: absolute; top: 14px;
    list-style: none; font-size: 14.5px; line-height: 18.5px;
  }
  .benefits-a { left: 198px; }
  .benefits-b { left: 450px; }
  .divider {
    position: absolute; left: 436px; top: 10px; width: 2px; height: 62px; background: #fff;
  }

  .map {
    position: absolute; left: 52px; top: 849px; width: 700px; height: 204px;
    background: linear-gradient(115deg, var(--map-base) 0%, var(--map-park) 30%, var(--map-base) 55%, var(--map-base) 75%, var(--map-park) 100%);
  }
  .map-frame { position: absolute; left: 0; top: 0; }

  .cta {
    position: absolute; left: 267px; top: 1080px; width: 267px; height: 57px;
    background: var(--orange); color: #fff;
    font-weight: 700; font-size: 21px;
    display: flex; align-items: center; justify-content: center;
  }
</style>
</head>
<body>
  <main class="flyer">
    <header class="header">
      <div class="brand"><span class="brand-dot"></span>Lernova</div>
      <div class="header-block contact">
        Contact Details:<br>
        Phone: 020 4719 8263<br>
        Email:&nbsp;&nbsp;enquiries@lernova.co.uk
      </div>
      <div class="header-block address">
        Address:<br>
        Kelbridge Business and Innovation Centre<br>
        Ashvale Court, Wrenfield Road, HA4 9QD
      </div>
    </header>

    <div class="illustration" role="img" aria-label="Open book with handwritten maths formulas rising from its pages"></div>

    <section class="headline-band">
      <h1 class="headline">Quality Private<br>Maths Tuition</h1>
    </section>
    <p class="subhead">GCSE, A-Levels,<br>11 Plus Exams</p>

    <section class="features">
      <div class="offer">FREE FIRST<br>SESSION</div>
      <ul class="benefits benefits-a">
        <li>Monthly Feedback reports</li>
        <li>Free support outside of sessions</li>
        <li>Clear Target grades</li>
      </ul>
      <span class="divider"></span>
      <ul class="benefits benefits-b">
        <li>Personalised Lesson plans</li>
        <li>Tangible Results</li>
      </ul>
    </section>

    <div class="map" role="img" aria-label="Street map showing the location of the Kelbridge Business and Innovation Centre">
      <svg class="map-frame" width="700" height="204" viewBox="0 0 700 204">
        <path d="M2 42 V2 H42" fill="none" stroke="var(--royal)" stroke-width="4"/>
        <path d="M698 162 V202 H658" fill="none" stroke="var(--royal)" stroke-width="4"/>
      </svg>
    </div>

    <div class="cta">www.lernova.co.uk</div>
  </main>
</body>
</html>
```